Soltravex business card

a nice business card with the logo,
Soltravex
Delia Vostrand
Marketing Director
CH-1296 Geneva
Switzerland
+41 79 612 3048
email: Delia.Vostrand@soltravex-mail.net

Target Market(s)

fertilizer business people, very nice and classic business card, normal size, make it nice and funky, try to make it different from the normal boring ones if possible.

Industry/Entity Type

Farming

Number of Pages Required

1 page

Requirements
Must have
• logo, Soltravex, my name - mail and phone number
regular business card size for me to print easy please

```html
<!DOCTYPE html>
<html lang="en">
<head>
<meta charset="utf-8">
<title>Soltravex business card</title>
<link rel="stylesheet" href="https://fonts.googleapis.com/css2?family=Arimo:wght@400&family=Open+Sans:wght@600&display=swap">
<style>
  :root {
    --leaf-green: #a9cf38;
    --ink-grey: #666666;
    --card-white: #ffffff;
    --card-edge: #2a2a2a;
    --page-bg: #ffffff;
  }
  html, body {
    margin: 0;
    padding: 0;
    width: 1080px;
    height: 1200px;
    overflow: hidden;
    background: var(--page-bg);
  }
  .canvas {
    position: relative;
    width: 1080px;
    height: 1200px;
  }
  .business-card {
    position: absolute;
    left: 190px;
    top: 59px;
    width: 700px;
    height: 1082px;
    box-sizing: border-box;
    background: var(--card-white);
    border: 1px solid var(--card-edge);
    overflow: hidden;
    font-family: "Arimo", Arial, sans-serif;
    color: var(--ink-grey);
  }
  .brand {
    position: absolute;
    left: 82px;
    top: 444px;
    display: flex;
    align-items: center;
    gap: 14px;
  }
  .brand-name {
    font-family: "Open Sans", Arial, sans-serif;
    font-weight: 600;
    font-size: 28px;
    line-height: 1;
    letter-spacing: 11px;
    color: var(--ink-grey);
    margin: 0;
  }
  .brand-dot {
    width: 14px;
    height: 14px;
    border-radius: 50%;
    background: var(--leaf-green);
  }
  .brand-rule {
    position: absolute;
    left: 73px;
    right: 0;
    top: 491px;
    height: 3px;
    background: var(--leaf-green);
  }
  .person-name {
    position: absolute;
    left: 82px;
    top: 634px;
    margin: 0;
    font-weight: 400;
    font-size: 43px;
    line-height: 1;
    letter-spacing: 0.3px;
  }
  .person-role {
    position: absolute;
    left: 82px;
    top: 694px;
    margin: 0;
    font-size: 33px;
    line-height: 1;
    letter-spacing: 1.5px;
  }
  .contact {
    position: absolute;
    left: 82px;
    top: 866px;
    margin: 0;
    font-style: normal;
    font-size: 27px;
    line-height: 39.5px;
  }
  .contact span { display: block; }
  .pattern-band {
    position: absolute;
    left: 0;
    bottom: 0;
    width: 627px;
    height: 74px;
    background: linear-gradient(90deg, var(--leaf-green), #bcdc62 50%, var(--leaf-green));
  }
</style>
</head>
<body>
  <main class="canvas">
    <article class="business-card">
      <div class="brand">
        <p class="brand-name">SOLTRAVEX</p>
        <span class="brand-dot"></span>
      </div>
      <div class="brand-rule"></div>

      <h1 class="person-name">Delia VOSTRAND</h1>
      <p class="person-role">Marketing Director</p>

      <address class="contact">
        <span>CH-1296 Geneva, Switzerland</span>
        <span>tel: +41 79 612 3048</span>
        <span>e-mail: Delia.Vostrand@soltravex-mail.net</span>
      </address>

      <div class="pattern-band" role="img" aria-label="Band of repeating green leaf-wave pattern"></div>
    </article>
  </main>
</body>
</html>
```